Mara Lindqvist Advisory Business Cards

Hi - using the information and logo provided I require a two sided business card designed with the following information. The business card is a 'mini card' 3.5" x 1.25".

Front of card should be the logo attached but inverted (so the background is the peach colour and the logo white).

Back should have these details. If we can't fit the Instragram and Facebook part can we just put the little logos.

Mara Lindqvist

Art and Design Consultant
Dealer - Curator - Events - Styling - Creative Sourcing

P: 0438 519 207
E: mara@maralindqvistadvisory.com
W: www.maralindqvistadvisory.com
I (instagram image please): maralindqvistadvisory F (Facebook image please): MaraLindqvistAdvisor

Target Market(s)

Galleries, artists, art buyers, interior design clients, event managers, creative types

Industry/Entity Type

Business

```html
<!DOCTYPE html>
<html lang="en">
<head>
<meta charset="utf-8">
<title>Mara Lindqvist Advisory – Mini Business Cards</title>
<link rel="stylesheet" href="https://fonts.googleapis.com/css2?family=Libre+Baskerville&display=swap">
<style>
  :root {
    --backdrop: #cbc5c1;
    --peach: #f0c6ad;
    --peach-light: #f3d0bc;
    --paper: #f4f1ee;
    --slate: #858080;
    --white: #ffffff;
    --ink-grey: #7d7878;
  }
  * { margin: 0; padding: 0; box-sizing: border-box; }
  html, body {
    width: 1200px;
    height: 789px;
    overflow: hidden;
    background: var(--backdrop);
    font-family: "Libre Baskerville", Georgia, serif;
  }
  .sheet {
    width: 1200px;
    height: 789px;
    display: flex;
    flex-direction: column;
    align-items: center;
    justify-content: center;
    gap: 64px;
  }
  .card {
    width: 840px;
    height: 300px;
    box-shadow: 0 10px 24px rgba(0, 0, 0, 0.12);
    position: relative;
    overflow: hidden;
  }

  /* Front */
  .card-front {
    background: linear-gradient(100deg, var(--peach) 0%, var(--peach-light) 100%);
    display: flex;
    flex-direction: column;
    align-items: center;
    justify-content: center;
  }
  .front-name {
    color: var(--white);
    font-size: 40px;
    letter-spacing: 0.12em;
    text-transform: uppercase;
    margin-top: 20px;
  }
  .front-web {
    position: absolute;
    bottom: 26px;
    color: var(--white);
    font-size: 15px;
    letter-spacing: 0.1em;
  }

  /* Back */
  .card-back {
    display: flex;
    background: var(--slate);
  }
  .back-brand {
    width: 300px;
    background: var(--paper);
    display: flex;
    align-items: center;
    justify-content: center;
    text-align: center;
    padding: 0 26px;
  }
  .brand-name {
    color: var(--ink-grey);
    font-size: 23px;
    line-height: 1.5;
    letter-spacing: 0.14em;
    text-transform: uppercase;
  }
  .back-details {
    flex: 1;
    padding: 14px;
  }
  .details-frame {
    height: 100%;
    border: 2px solid var(--white);
    padding: 22px 28px;
    color: var(--white);
  }
  .person-name {
    font-size: 27px;
    letter-spacing: 0.04em;
    margin-bottom: 10px;
  }
  .person-role {
    font-size: 12.5px;
    line-height: 1.6;
    letter-spacing: 0.04em;
    margin-bottom: 16px;
  }
  .contact-list { list-style: none; }
  .contact-list li {
    display: flex;
    align-items: center;
    gap: 12px;
    font-size: 15px;
    line-height: 1;
    margin-bottom: 7px;
  }
  .contact-icon {
    width: 18px;
    height: 18px;
    flex: none;
  }
</style>
</head>
<body>
<main class="sheet">

  <section class="card card-front" aria-label="Card front">
    <p class="front-name">Mara Lindqvist Advisory</p>
    <p class="front-web">www.maralindqvistadvisory.com</p>
  </section>

  <section class="card card-back" aria-label="Card back">
    <div class="back-brand">
      <p class="brand-name">Mara Lindqvist Advisory</p>
    </div>
    <div class="back-details">
      <div class="details-frame">
        <h1 class="person-name">Mara Lindqvist</h1>
        <p class="person-role">Art and Design Consultant<br>Dealer - Curator - Events - Styling - Creative Sourcing</p>
        <ul class="contact-list">
          <li>
            <svg class="contact-icon" viewBox="0 0 18 18" aria-hidden="true">
              <rect width="18" height="18" fill="#f0c6ad"/>
              <path d="M5 4h2.5l1 3-1.5 1a6 6 0 0 0 3 3l1-1.5 3 1V13a1 1 0 0 1-1 1A9 9 0 0 1 4 5a1 1 0 0 1 1-1z" fill="#858080"/>
            </svg>
            0438 519 207
          </li>
          <li>
            <svg class="contact-icon" viewBox="0 0 18 18" aria-hidden="true">
              <rect width="18" height="18" fill="#f0c6ad"/>
              <rect x="3.5" y="5" width="11" height="8" fill="none" stroke="#858080" stroke-width="1.3"/>
              <path d="M3.5 5l5.5 4.5L14.5 5" fill="none" stroke="#858080" stroke-width="1.3"/>
            </svg>
            mara@maralindqvistadvisory.com
          </li>
          <li>
            <svg class="contact-icon" viewBox="0 0 18 18" aria-hidden="true">
              <rect width="18" height="18" fill="#f0c6ad"/>
              <circle cx="9" cy="9" r="5.2" fill="none" stroke="#858080" stroke-width="1.2"/>
              <ellipse cx="9" cy="9" rx="2.3" ry="5.2" fill="none" stroke="#858080" stroke-width="1"/>
              <path d="M3.8 9h10.4" stroke="#858080" stroke-width="1"/>
            </svg>
            www.maralindqvistadvisory.com
          </li>
          <li>
            <svg class="contact-icon" viewBox="0 0 18 18" aria-hidden="true">
              <rect width="18" height="18" fill="#f0c6ad"/>
            </svg>
            maralindqvistadvisory
          </li>
          <li>
            <svg class="contact-icon" viewBox="0 0 18 18" aria-hidden="true">
              <rect width="18" height="18" fill="#f0c6ad"/>
            </svg>
            MaraLindqvistAdvisor
          </li>
        </ul>
      </div>
    </div>
  </section>

</main>
</body>
</html>
```